New Webpage for High Class Expert Witness Services Company

We are looking for a minimalist design for a webpage that just has our logo and an entry form offer to connect with one of our Liaisons.
The entry form should just ask for Name, Email, Contact Info and Description of Project.

Company Name is: The Marlow Crest Advisory Services

Number of Pages Required

1 page

```html
<!DOCTYPE html>
<html lang="en">
<head>
<meta charset="UTF-8">
<title>The Marlow Crest Advisory Services — Contact</title>
<link rel="stylesheet" href="https://fonts.googleapis.com/css2?family=EB+Garamond:wght@400;500&display=swap">
<style>
  :root {
    --ink: #111111;
    --label: #555555;
    --field: #e7e7e9;
    --rule: #8a8a8a;
    --paper: #ffffff;
    --photo-navy: #1f2d45;
    --photo-grey: #7d848c;
    --photo-light: #c9ccd0;
  }
  * { box-sizing: border-box; margin: 0; padding: 0; }
  html, body { width: 1200px; height: 675px; overflow: hidden; background: var(--paper); }
  body { position: relative; font-family: "EB Garamond", Georgia, serif; color: var(--ink); }

  .site-header {
    position: absolute; left: 0; top: 0; width: 1200px; height: 58px;
    border-bottom: 1px solid var(--rule);
  }
  .brand {
    position: absolute; left: 92px; top: 19px;
    display: flex; align-items: center; gap: 8px;
    font-size: 16px; font-weight: 500; letter-spacing: 0.04em;
    text-transform: uppercase; color: var(--ink);
  }
  .brand-mark { width: 14px; height: 14px; background: var(--ink); }
  .menu-toggle { position: absolute; left: 1075px; top: 20px; }

  .headline {
    position: absolute; left: 92px; top: 124px;
    font-size: 50px; font-weight: 400; line-height: 60px;
    letter-spacing: 0.005em; text-transform: uppercase;
  }

  .contact-form label {
    position: absolute; font-size: 13.5px; color: var(--label);
  }
  .contact-form .field {
    position: absolute; height: 40px; width: 247px;
    background: var(--field); border: none; border-radius: 6px;
  }
  .contact-form .field-area { width: 500px; height: 106px; }
  .submit {
    position: absolute; left: 92.5px; top: 542.5px; width: 500px; height: 40px;
    background: var(--ink); color: var(--paper); border: none; border-radius: 6px;
    font-family: "EB Garamond", Georgia, serif; font-size: 16px; letter-spacing: 0.02em;
  }

  .hero-photo {
    position: absolute; left: 667px; top: 58px; width: 533px; height: 546px;
    border-bottom-left-radius: 32px;
    background:
      radial-gradient(ellipse at 72% 70%, var(--photo-navy) 0 38%, transparent 60%),
      linear-gradient(100deg, var(--photo-grey) 0%, #5d6670 35%, #9aa1a8 70%, var(--photo-light) 100%);
  }
</style>
</head>
<body>
  <header class="site-header">
    <div class="brand"><span class="brand-mark"></span>The Marlow Crest Advisory Services</div>
    <svg class="menu-toggle" width="28" height="20" viewBox="0 0 28 20" aria-label="Menu">
      <rect x="0" y="0" width="28" height="1.6" fill="#111"/>
      <rect x="0" y="9" width="28" height="1.6" fill="#111"/>
      <rect x="0" y="18" width="28" height="1.6" fill="#111"/>
    </svg>
  </header>

  <h1 class="headline">Focused Protection.<br>Trusted Expertise.</h1>

  <form class="contact-form">
    <label style="left:92.5px;top:251px;">First Name</label>
    <input class="field" style="left:92.5px;top:277px;">
    <label style="left:345.5px;top:251px;">Last Name</label>
    <input class="field" style="left:345.5px;top:277px;">

    <label style="left:92.5px;top:321px;">Email</label>
    <input class="field" style="left:92.5px;top:347px;">
    <label style="left:345.5px;top:321px;">Contact Info</label>
    <input class="field" style="left:345.5px;top:347px;">

    <label style="left:92.5px;top:391px;">Description of Project</label>
    <textarea class="field field-area" style="left:92.5px;top:417px;"></textarea>

    <button class="submit" type="submit">SUBMIT</button>
  </form>

  <div class="hero-photo" role="img" aria-label="Photo of a smiling businesswoman in a navy suit on a phone call, with a colleague reading a tablet behind her outside an office building"></div>
</body>
</html>
```